Introduction brochure for IT Company

We need a brochure for introducing our new small business services to the market.

We need a template that we can alter and play with as services change, and was thinking about the following:

A front page which has logo (attached), and follows colour scheme used on our website www.quillotech.com.au, that has a small description of the service/or us, we are introducing and Call us on 1300 627 398 at the bottom of page.
For the first print only front page and back page will be used, as we are still refining the service. We will be introducing the company to new prospects face to face and want to leave them with a small brochure which explains what we do for them, and clear contact details.

Middle section we have not worked out fully yet, as it depends on space available, but please use points under service on our website for now to fill in with some points.

Last page we want to have the last 1/3 of page to be our contact details along with a google map of our location etc. like the contact us page on website.

We prefer to stay on the lighter side, so more playful in style but you guys are the experts.

Target Market(s)

Small business 1-10 Employees

Industry/Entity Type

It Company

Font styles to use
Serif

Requirements
Must have
• Clear contact details, playful design which is easy to read. Follow colour scheme or close to website, www.quillotech.com.au, as this is reflected in all our marketing. Some artistic license is of course given.
Nice to have
• Nothing comes to mind, go crazy and make it fun.
Should not have
• typical images of large scale server racks and enterprise level images. Stay small business.

```html
<!DOCTYPE html>
<html lang="en">
<head>
<meta charset="utf-8">
<title>Quillotech – Brochure</title>
<link href="https://fonts.googleapis.com/css2?family=Titillium+Web:ital,wght@0,400;0,600;0,700;1,400&display=swap" rel="stylesheet">
<style>
:root{
  --red:#e21e26;
  --dark:#232323;
  --ink:#1f1f1f;
  --muted:#cfcfcf;
  --bubble:#e3e3e3;
  --stage:#ebebeb;
  --white:#ffffff;
}
*{box-sizing:border-box;margin:0;padding:0}
html,body{width:1200px;height:826px;overflow:hidden}
body{background:var(--stage);font-family:"Titillium Web",sans-serif;color:var(--ink);position:relative}
.page{position:absolute;top:42px;width:526px;height:743px;overflow:hidden}
.page--front{left:50px;background:var(--white)}
.page--back{left:621px;background:var(--dark);color:var(--white)}

/* shared */
.top-strip{position:absolute;left:0;top:0;width:100%;height:15px;background:var(--red)}
.brand{position:absolute;top:0;height:71px;background:var(--red);display:flex;align-items:center;gap:7px;color:var(--white);font-weight:700;font-size:20px;letter-spacing:.5px;white-space:nowrap}
.brand__dot{flex:0 0 10px;width:10px;height:10px;background:var(--white);border-radius:50%}
.page--front .brand{left:0;width:178px;padding-left:20px;clip-path:polygon(0 0,100% 0,82% 100%,0 100%)}
.page--back .brand{right:0;width:182px;padding-left:36px;font-size:18px;clip-path:polygon(0 0,100% 0,100% 100%,16% 100%)}

/* front: hero */
.hero{position:absolute;left:0;top:15px;width:100%;height:209px;background:linear-gradient(90deg,#f6f6f6,#ececec)}
.hero__photo{position:absolute;right:0;top:0;width:250px;height:209px;background:linear-gradient(135deg,#d9c3a6 0%,#e9dcd0 45%,#cbc9d8 100%)}
.hero__text{position:absolute;left:22px;top:112px}
.hero__name{font-weight:700;font-size:17px;line-height:20px}
.hero__lead{font-size:17px;line-height:20px}
.hero__target{color:var(--red);font-weight:700;font-size:22px;line-height:26px}

/* front: about */
.about{position:absolute;left:0;top:224px;width:100%;height:181px;background:var(--dark);color:var(--white);text-align:center}
.about__label{position:absolute;left:213px;top:22px;width:100px;height:24px;background:var(--red);clip-path:polygon(8% 0,100% 0,92% 100%,0 100%);font-weight:700;font-size:15px;line-height:24px}
.about__body{position:absolute;left:33px;top:58px;width:460px;font-size:10.3px;line-height:14px}

/* front: columns */
.col-title{font-size:18px;font-weight:600;line-height:22px}
.col-rule{width:115px;height:3px;background:var(--red);margin-top:8px}
.why{position:absolute;left:19px;top:426px;width:240px}
.why__list{list-style:none;margin-top:14px}
.why__item{display:flex;gap:8px;font-size:11.5px;line-height:13px;margin-bottom:11px}
.why__item svg{flex:0 0 11px;margin-top:1px}
.why__item strong{color:var(--red)}
.clients{position:absolute;left:297px;top:426px;width:210px}
.quote{position:absolute;left:287px;top:477px;width:220px;height:157px;background:var(--bubble);border-radius:12px;padding:10px 12px;font-style:italic;font-size:8.3px;line-height:13.8px;color:#444}
.quote__tail{position:absolute;left:302px;top:633px}
.quote__name{position:absolute;right:21px;top:640px;color:var(--red);font-size:12px;font-weight:600}

/* front: footer */
.front-foot{position:absolute;left:0;top:673px;width:100%;height:70px}
.front-foot__band{position:absolute;right:0;top:0;width:240px;height:57px;background:var(--red);clip-path:polygon(13% 0,100% 0,100% 100%,0 100%)}
.front-foot__base{position:absolute;left:0;bottom:0;width:100%;height:13px;background:var(--red)}
.call-small{position:absolute;left:20px;top:16px;font-weight:700;font-size:13px}
.call-box{position:absolute;left:86px;top:8px;width:167px;height:33px;border:1.5px solid var(--ink);border-radius:8px;display:flex;align-items:center;gap:3px;padding-left:4px;font-weight:700;font-size:23px;white-space:nowrap}
.contact{position:absolute;left:301px;top:6px;color:var(--white);font-size:10px;line-height:16px}
.contact__row{display:flex;align-items:center;gap:7px}

/* back */
.services-title{position:absolute;left:22px;top:32px;font-weight:700;font-size:17px}
.service{position:absolute;display:flex;gap:12px}
.service__icon{flex:0 0 44px}
.service__title{color:var(--red);font-weight:600;font-size:10px;line-height:14px}
.service__body{font-size:7.5px;line-height:11.5px;color:#e6e6e6;margin-top:3px}
.callbar{position:absolute;left:22px;top:490px;width:482px;height:43px;background:var(--red);border-radius:4px;display:flex;align-items:center;justify-content:center;gap:8px;font-weight:700;font-size:27px;letter-spacing:.5px}
.map{position:absolute;left:22px;top:539px;width:479px;height:161px;border-radius:5px;background:linear-gradient(135deg,#eeeeee,#dedede)}
.back-foot{position:absolute;left:22px;top:709px;width:482px;display:flex;justify-content:space-between;font-size:9.3px}
.back-foot span{display:flex;align-items:center;gap:4px}
</style>
</head>
<body>

<section class="page page--front">
  <div class="hero">
    <div class="hero__photo" role="img" aria-label="Photo of a mother and young daughter smiling at a laptop"></div>
  </div>
  <div class="top-strip"></div>
  <div class="brand"><span class="brand__dot"></span>QUILLOTECH</div>

  <div class="hero__text">
    <p class="hero__name">QUILLOTECH</p>
    <p class="hero__lead">provide a wide range of services to</p>
    <p class="hero__target">HOME AND OFFICE USERS.</p>
  </div>

  <div class="about">
    <div class="about__label">ABOUT US</div>
    <p class="about__body">Quillotech is your one stop shop for all your IT needs. We do it all, from simple hardware/software sales to complete network installations. We have experts in every area of IT, we'll help you set up a home computer, set up complicated networks for small businesses and create your professional cloud based network. Our experts are great at what they do, but they're also great at explaining it. Whatever your tech background is our staff can walk you through exactly what they are doing. By remaining independent we are able to sell you any product which means our IT solutions are designed to suit you using the appropriate and cost effective hardware/software solutions.</p>
  </div>

  <div class="why">
    <h2 class="col-title">Why Choose Us?</h2>
    <div class="col-rule"></div>
    <ul class="why__list">
      <li class="why__item"><svg width="11" height="10" viewBox="0 0 11 10"><path d="M1 5l3 3 6-7" fill="none" stroke="#e21e26" stroke-width="2.4"/></svg><span>No fix, no charge policy.</span></li>
      <li class="why__item"><svg width="11" height="10" viewBox="0 0 11 10"><path d="M1 5l3 3 6-7" fill="none" stroke="#e21e26" stroke-width="2.4"/></svg><span>Friendly, highly knowledgeable staff - all questions answered.</span></li>
      <li class="why__item"><svg width="11" height="10" viewBox="0 0 11 10"><path d="M1 5l3 3 6-7" fill="none" stroke="#e21e26" stroke-width="2.4"/></svg><span>We'll take care of everything from the first installation to IT support- all your needs from one expert.</span></li>
      <li class="why__item"><svg width="11" height="10" viewBox="0 0 11 10"><path d="M1 5l3 3 6-7" fill="none" stroke="#e21e26" stroke-width="2.4"/></svg><span>Professional quality advice on the best way to use and care for your systems</span></li>
      <li class="why__item"><svg width="11" height="10" viewBox="0 0 11 10"><path d="M1 5l3 3 6-7" fill="none" stroke="#e21e26" stroke-width="2.4"/></svg><span>Obligation-free quotes - get yours now.</span></li>
      <li class="why__item"><svg width="11" height="10" viewBox="0 0 11 10"><path d="M1 5l3 3 6-7" fill="none" stroke="#e21e26" stroke-width="2.4"/></svg><span>Over 65? <strong>GET DISCOUNT 10%</strong></span></li>
    </ul>
  </div>

  <div class="clients">
    <h2 class="col-title">What Clients Say?</h2>
    <div class="col-rule"></div>
  </div>
  <blockquote class="quote">Quillotech is a fantastic company with an immense ammount of experience and knowledge about technologies and computers. Their assistance has been exceptional across the board! Assitance has for example included loading a new operating system, dealing with the fibre and computer services within a gated community that has had many issues, and transferring materials from an old laptop to a new tablet. In addition, major issues with Wifi and Security were addressed and even rescued. I am telling everyone to call Tom!</blockquote>
  <svg class="quote__tail" width="20" height="14" viewBox="0 0 20 14"><path d="M0 0h20L6 14z" fill="#e3e3e3"/></svg>
  <p class="quote__name">Dr Maren Holloway-Tate</p>

  <footer class="front-foot">
    <div class="front-foot__band"></div>
    <div class="front-foot__base"></div>
    <span class="call-small">Call Us on</span>
    <div class="call-box">
      <svg width="14" height="26" viewBox="0 0 14 26"><path d="M4 1h4v6H5c-1 4-1 8 0 12h3v6H4C0 19 0 7 4 1z" fill="#1f1f1f"/></svg>
      1300 627 398
    </div>
    <div class="contact">
      <div class="contact__row"><svg width="8" height="10" viewBox="0 0 8 10"><path d="M4 0a4 4 0 014 4c0 3-4 6-4 6S0 7 0 4a4 4 0 014-4z" fill="#fff"/><circle cx="4" cy="4" r="1.5" fill="#e21e26"/></svg>14/58 Harlow Street, Kelvin Park TAS 7019</div>
      <div class="contact__row"><svg width="9" height="7" viewBox="0 0 9 7"><rect width="9" height="7" fill="#fff"/><path d="M0 0l4.5 4L9 0" fill="none" stroke="#e21e26"/></svg>service@quillotech.com.au</div>
      <div class="contact__row"><svg width="9" height="9" viewBox="0 0 9 9"><circle cx="4.5" cy="4.5" r="4" fill="none" stroke="#fff"/><path d="M.5 4.5h8M4.5.5c-2 2-2 6 0 8M4.5.5c2 2 2 6 0 8" fill="none" stroke="#fff" stroke-width=".8"/></svg>www.quillotech.com.au</div>
    </div>
  </footer>
</section>

<section class="page page--back">
  <div class="top-strip"></div>
  <div class="brand"><span class="brand__dot"></span>QUILLOTECH</div>
  <h2 class="services-title">OUR SERVICES</h2>

  <div class="service" style="left:21px;top:86px;width:240px">
    <svg class="service__icon" width="44" height="42" viewBox="0 0 44 42"><rect x="0" y="4" width="10" height="34" rx="1" fill="#e21e26"/><rect x="13" y="2" width="30" height="24" rx="2" fill="#e21e26"/><rect x="16" y="5" width="24" height="18" fill="#232323"/><rect x="24" y="26" width="8" height="8" fill="#e21e26"/><rect x="18" y="34" width="20" height="3" fill="#e21e26"/></svg>
    <div><p class="service__title">Computer hardware and software installations and troubleshooting</p><p class="service__body">Whatever computer problems you're experiencing, whether hardware or software related, we can fix it. Our highly skilled technicians specialise in all type of hardware and software installations, and make configurations to suit your needs.</p></div>
  </div>

  <div class="service" style="left:21px;top:211px;width:240px">
    <svg class="service__icon" width="44" height="36" viewBox="0 0 44 36"><path d="M3 12a27 27 0 0138 0M9 18a18 18 0 0126 0M15 24a9 9 0 0114 0" fill="none" stroke="#e21e26" stroke-width="4" stroke-linecap="round"/><circle cx="22" cy="31" r="3.5" fill="#e21e26"/></svg>
    <div><p class="service__title">Internet installations and advice</p><p class="service__body">We can advise you on which broadband or fibre plan would suit your usage, to make sure you are not paying too much for your internet service. Our internet installation is a straightforward process - we will set it all up for you, so you don't have to worry about anything except getting online and doing what you need to. Easy!</p></div>
  </div>

  <div class="service" style="left:21px;top:330px;width:240px">
    <svg class="service__icon" width="44" height="42" viewBox="0 0 44 42"><ellipse cx="18" cy="7" rx="16" ry="6" fill="#e21e26"/><path d="M2 11c0 4 32 4 32 0v6c0 4-32 4-32 0zM2 21c0 4 32 4 32 0v6c0 4-32 4-32 0z" fill="#e21e26"/><circle cx="32" cy="30" r="9" fill="#232323" stroke="#e21e26" stroke-width="3"/><path d="M27 26l-1 5 5-1" fill="none" stroke="#e21e26" stroke-width="2"/></svg>
    <div><p class="service__title">Data backup and recovery</p><p class="service__body">Never lose data again! We have backup solutions to suit any home or business requirement. Our solutions will ensure that your vital information will still be safe, should the worst happen.</p></div>
  </div>

  <div class="service" style="left:21px;top:413px;width:240px">
    <svg class="service__icon" width="44" height="40" viewBox="0 0 44 40"><circle cx="8" cy="7" r="5" fill="#e21e26"/><path d="M2 14h12l10 8-2 3-8-5v18H2z" fill="#e21e26"/><path d="M22 6l18 0-6 24h-8" fill="none" stroke="#e21e26" stroke-width="3"/><rect x="14" y="35" width="30" height="3" fill="#e21e26"/></svg>
    <div><p class="service__title">IT training</p><p class="service__body">We can help you learn about your computer hardware or software. We also offer training on any new purchase you make for your computer, from your monitor to your HD video cam.</p></div>
  </div>

  <div class="service" style="left:285px;top:86px;width:222px">
    <svg class="service__icon" width="44" height="48" viewBox="0 0 44 48"><rect x="6" y="0" width="32" height="48" rx="4" fill="#e21e26"/><rect x="10" y="5" width="24" height="5" fill="#232323"/><rect x="10" y="14" width="24" height="5" fill="#232323"/><circle cx="22" cy="36" r="4" fill="#232323"/></svg>
    <div><p class="service__title">Custom built computer service</p><p class="service__body">Anywhere in Hobart, our consultants and technicians will help you choose a system that is perfect for your usage. Often people spend more money than they need to because a salesperson has pointed them in the wrong direction. At Quillotech, our computer service stands out because we pride ourselves on getting to know our customers' needs and building solutions to suit them.</p></div>
  </div>

  <div class="service" style="left:285px;top:222px;width:222px">
    <svg class="service__icon" width="44" height="40" viewBox="0 0 44 40"><path d="M8 2h28l4 12H4z" fill="#e21e26"/><rect x="16" y="5" width="12" height="5" fill="#232323"/><rect x="0" y="16" width="44" height="12" rx="4" fill="#e21e26"/><circle cx="9" cy="22" r="2" fill="#232323"/><circle cx="17" cy="22" r="2" fill="#232323"/><circle cx="25" cy="22" r="2" fill="#232323"/><circle cx="33" cy="22" r="2" fill="#232323"/><rect x="20" y="28" width="4" height="8" fill="#e21e26"/><rect x="12" y="36" width="20" height="3" fill="#e21e26"/></svg>
    <div><p class="service__title">Wired and wireless network installations and advice</p><p class="service__body">We can get your new home or business network functioning better and faster by optimising the way things are connected and performing an internal clean up on your computer. Whether wired or wireless, our network installation is quick and effective.</p></div>
  </div>

  <div class="service" style="left:285px;top:331px;width:222px">
    <svg class="service__icon" width="44" height="46" viewBox="0 0 44 46"><path d="M22 0l20 7v14c0 12-9 21-20 25C11 42 2 33 2 21V7z" fill="#e21e26"/><path d="M12 22l8 8 13-14" fill="none" stroke="#232323" stroke-width="4.5"/></svg>
    <div><p class="service__title">Computer and network IT security services</p><p class="service__body">60% of computers in Australia today do not have adequate security. We have solutions for any type of computer or network to make sure your system is protected at all times from the malware and viruses. IT security services are completely essential</p></div>
  </div>

  <div class="callbar">CALL US ON
    <svg width="22" height="22" viewBox="0 0 22 22"><path d="M5 1l4 5-2 3c1 3 3 5 6 6l3-2 5 4-3 4C9 21 1 13 1 4z" fill="#fff"/></svg>
    1300 627 398</div>

  <div class="map" role="img" aria-label="Street map showing the office location at 14/58 Harlow Street, Kelvin Park"></div>

  <div class="back-foot">
    <span><svg width="7" height="9" viewBox="0 0 8 10"><path d="M4 0a4 4 0 014 4c0 3-4 6-4 6S0 7 0 4a4 4 0 014-4z" fill="#e21e26"/></svg>14/58 Harlow Street, Kelvin Park TAS 7019</span>
    <span><svg width="9" height="7" viewBox="0 0 9 7"><rect width="9" height="7" fill="#e21e26"/><path d="M0 0l4.5 4L9 0" fill="none" stroke="#232323"/></svg>service@quillotech.com.au</span>
    <span><svg width="9" height="9" viewBox="0 0 9 9"><circle cx="4.5" cy="4.5" r="4" fill="none" stroke="#e21e26"/><path d="M.5 4.5h8" stroke="#e21e26"/></svg>www.quillotech.com.au</span>
  </div>
</section>

</body>
</html>
```